Natural Australian skin care company packaging for new product Bath salts

We are moving to fully refillable packaging and need someone to design our refill pouches. we have a number of products we need to do this for but our first one is our natural bath salts. This comes in a 200g tin in a pouch then the pouch can be bought to refill the tin. We can either print on the pouch or do sickers. The tin is a simple matt black tin with white text on the lid. the pouch comes in a gold colour. pictures are in the drop box lid.
Luxury bath salts Pouch - the dimensions are 60*55*180mm, , we can either print directly or do a sticker, We also need the sleeve to go around the tin. The dimensions of the tin are 65x65x70mm. The same text needs to go onto the sleeve as the pouch. The tin is black with white printing on the top (see picture).
Text is as follows
VT logo Hum along moss 100% pure magnesium bath salts
A rich fragrance of Australian wild flowers (using natural essential oils) with frangipani and gardenia. Sink into the natural ancient salt lake sourced 100% pure magnesium to replenish your skin. Transdermal absorption of magnesium is effective and contributes to electrolyte balance, normal muscle function and aids calcium absorption. The ultimate mineral reset.
Directions: Fill bath, once full put two heaped tablespoons of the salts into the bath (approx 50g). Climb in and relax.
Velka Tonic full logo
Country of Origin: Australia
PO Box 318
Marlow Ridge 4592
QLD Australia
www.velkatonic.example
ingredients:
magnesium chloride *, parfum **
*naturally sourced from ancient salt lakes
**a combination of essential oils and natural isolates.
e: 200g / 7.05 Oz
We also need the recycle, plastic free, not tested on animal eco friendly symbols.
Please use this link to our press assets and tin and pouch photos.
https://www.filecrate.example/s/kq81xv3tmw0pd47/BXcLp9__wQzNtd?dl=0

```html
<!DOCTYPE html>
<html lang="en">
<head>
<meta charset="utf-8">
<title>Velka Tonic – Magnesium Bath Salts Label</title>
<link rel="stylesheet" href="https://fonts.googleapis.com/css2?family=Arvo:wght@400;700&family=Zilla+Slab:wght@300;400;600&family=Josefin+Sans:wght@400&display=swap">
<style>
  :root {
    --label-black: #000000;
    --label-white: #ffffff;
    --page-bg: #ffffff;
    --soft-white: #e8e8e8;
  }
  * { margin: 0; padding: 0; box-sizing: border-box; }
  html, body {
    width: 1200px; height: 720px; overflow: hidden;
    background: var(--page-bg);
  }
  .canvas { position: relative; width: 1200px; height: 720px; }

  .label {
    position: absolute; left: 440px; top: 20px;
    width: 321px; height: 680px;
    background: var(--label-black);
    color: var(--label-white);
    font-family: "Zilla Slab", Georgia, serif;
  }
  .label > * { position: absolute; left: 35px; }

  .closure-tab {
    left: auto; right: 30px; top: 0;
    width: 30px; height: 86px;
    background: var(--label-white);
  }

  .brand-square {
    top: 40px; width: 54px; height: 54px;
    background: var(--label-white);
  }
  .brand-name {
    top: 112px;
    font-family: "Arvo", Georgia, serif; font-weight: 700;
    font-size: 27px; letter-spacing: 0.3px; line-height: 1;
    white-space: nowrap;
  }
  .brand-tagline {
    top: 146px;
    font-family: "Arvo", Georgia, serif; font-weight: 400;
    font-size: 9px; letter-spacing: 0.2px;
  }
  .rule { width: 223px; height: 2px; background: var(--label-white); }
  .rule--top { top: 168px; }
  .rule--bottom { top: 404px; }

  .strength {
    top: 186px;
    font-family: "Arvo", Georgia, serif; font-weight: 700;
    font-size: 40px; line-height: 1;
  }
  .product-name {
    top: 236px;
    font-family: "Arvo", Georgia, serif; font-weight: 400;
    font-size: 22px; line-height: 28px; letter-spacing: 0.3px;
  }

  .description, .directions, .ingredients {
    font-size: 6.8px; line-height: 8.5px; letter-spacing: 1.1px;
    font-weight: 400; width: 230px;
  }
  .description { top: 310px; }
  .directions { top: 431px; }
  .ingredients { top: 481px; }
  .section-title { font-weight: 600; letter-spacing: 1.3px; }
  .footnotes {
    display: block; margin-top: 5px;
    font-size: 4.8px; line-height: 6px; letter-spacing: 0.6px;
  }

  .footer-brand { top: 551px; }
  .footer-brand__name {
    font-family: "Arvo", Georgia, serif; font-weight: 700;
    font-size: 7.5px; line-height: 1;
  }
  .footer-brand__tagline {
    font-family: "Arvo", Georgia, serif; font-size: 3.6px; letter-spacing: 0.2px;
    margin-top: 2px;
  }
  .address {
    top: 581px;
    font-size: 6.4px; line-height: 8.4px; font-weight: 300;
  }

  .eco-marks { top: 627px; display: flex; gap: 8px; align-items: center; }

  .net-weight {
    left: 186px; top: 638px;
    font-family: "Josefin Sans", Arial, sans-serif;
    font-size: 10px; letter-spacing: 0.2px;
  }
</style>
</head>
<body>
<main class="canvas">
  <section class="label">
    <div class="closure-tab"></div>

    <div class="brand-square" aria-hidden="true"></div>
    <h1 class="brand-name">VELKA TONIC</h1>
    <p class="brand-tagline">AUSTRALIAN BUSH MEDICINES</p>
    <div class="rule rule--top"></div>

    <p class="strength">100%</p>
    <h2 class="product-name">PURE MAGNESIUM<br>BATH SALTS</h2>

    <p class="description">
      A rich fragrance of Australian wild flowers (using natural essential oils) with frangipani and gardenia. Sink into the natural ancient salt lake sourced 100% pure magnesium to replenish your skin. Transdermal absorption of magnesium is effective and contributes to electrolyte balance, normal muscle function and aids calcium absorption. The ultimate mineral reset.
    </p>
    <div class="rule rule--bottom"></div>

    <p class="directions">
      <span class="section-title">Directions:</span><br>
      Fill bath, once full put two heaped tablespoons of the salts into the bath (approx 50g). Climb in and relax.
    </p>

    <p class="ingredients">
      <span class="section-title">Ingredients:</span><br>
      magnesium chloride *, parfum **
      <span class="footnotes">*naturally sourced from ancient salt lakes<br>**a combination of essential oils and natural isolates.</span>
    </p>

    <div class="footer-brand">
      <p class="footer-brand__name">VELKA TONIC</p>
      <p class="footer-brand__tagline">AUSTRALIAN BUSH MEDICINES</p>
    </div>

    <address class="address" style="font-style:normal">
      Country of Origin: Australia<br>
      PO Box 318<br>
      Marlow Ridge 4592<br>
      QLD Australia<br>
      www.velkatonic.example
    </address>

    <div class="eco-marks">
      <svg width="22" height="22" viewBox="0 0 22 22" role="img" aria-label="Recyclable mark">
        <circle cx="11" cy="11" r="9.5" fill="none" stroke="var(--label-white)" stroke-width="1.4"/>
      </svg>
      <svg width="22" height="22" viewBox="0 0 22 22" role="img" aria-label="Not tested on animals mark">
        <circle cx="11" cy="11" r="9.5" fill="none" stroke="var(--label-white)" stroke-width="1.4"/>
        <circle cx="11" cy="11" r="6.5" fill="none" stroke="var(--label-white)" stroke-width="0.8"/>
      </svg>
      <svg width="18" height="24" viewBox="0 0 18 24" role="img" aria-label="Plastic free mark">
        <rect x="1" y="1" width="16" height="22" fill="none" stroke="var(--label-white)" stroke-width="1.4"/>
      </svg>
    </div>

    <p class="net-weight">e: 200g / 7.05 Oz</p>
  </section>
</main>
</body>
</html>
```